Clear tides coaching programme

I need a flyer designed to promote my coaching programme. The programme is designed to help people who are feeling a bit lost in their life, looking for new possiblities or that they want more focus in their goals. It is an intensive programme designed to help people achieve real change in their lives. It is a premium product targeted at senior managers, directors and business leaders. I care passionately about helping people achieve their potential. I would like the design to fit with the logo (attached) and I've drafted the content (also attached). I would like it to be A5 and affordable to print - so not full colour.

```html
<!DOCTYPE html>
<html lang="en">
<head>
<meta charset="utf-8">
<title>Clear tides coaching programme – flyer</title>
<link rel="stylesheet" href="https://fonts.googleapis.com/css2?family=Oswald:wght@400;500&family=Open+Sans:ital,wght@0,300;0,400;0,700;1,300;1,700&display=swap">
<style>
  :root {
    --teal: #1a9e86;
    --purple: #3c1a6b;
    --ink: #3a3a3a;
    --grey-text: #555555;
    --ring-light: #f1f1f1;
    --ring-mid: #dcdcdc;
    --white: #ffffff;
  }
  * { box-sizing: border-box; margin: 0; padding: 0; }
  html, body { width: 845px; height: 1200px; overflow: hidden; background: var(--white); }
  .flyer {
    position: relative; width: 845px; height: 1200px; overflow: hidden;
    background: var(--white); font-family: "Open Sans", Arial, sans-serif; color: var(--ink);
  }
  .backdrop { position: absolute; inset: 0; }

  .are-you {
    position: absolute; left: 38px; top: 172px;
    font-family: "Open Sans", Arial, sans-serif; font-weight: 700; font-style: italic;
    font-size: 26px; color: var(--white);
  }

  .question {
    position: absolute; width: 216px; text-align: center;
    font-family: "Oswald", "Arial Narrow", sans-serif; font-weight: 500;
    font-size: 25px; line-height: 29px; color: var(--white); text-transform: uppercase;
  }
  .question--top    { left: 315px; top: 110px; }
  .question--left   { left: 24px;  top: 365px; }
  .question--right  { left: 617px; top: 366px; }
  .question--bottom { left: 315px; top: 584px; }

  .quote {
    position: absolute; left: 270px; top: 410px; width: 306px; text-align: center;
    font-weight: 700; font-size: 16px; line-height: 22px; color: var(--grey-text);
  }
  .quote cite {
    display: block; text-align: right; font-style: normal; font-weight: 400;
    padding-right: 16px;
  }

  .brand {
    position: absolute; left: 640px; top: 92px; width: 175px; text-align: center;
  }
  .brand__dot {
    display: block; width: 58px; height: 58px; margin: 0 auto 12px;
    border-radius: 50%; background: var(--teal);
  }
  .brand__name {
    font-family: "Open Sans", Arial, sans-serif; font-weight: 400; color: var(--purple);
    font-size: 17px; line-height: 24px; text-transform: uppercase;
  }

  .programme {
    position: absolute; left: 44px; top: 614px; width: 372px;
    font-weight: 300; font-size: 15.5px; line-height: 22.5px; color: var(--ink);
  }
  .programme p + p { margin-top: 10px; }
  .programme strong { font-weight: 700; }
  .programme .highlight { font-weight: 400; }
  .programme em { font-weight: 400; font-style: italic; }

  .divider { position: absolute; left: 412px; top: 820px; width: 1px; height: 226px; background: #cfcfcf; }

  .about { position: absolute; left: 438px; top: 812px; width: 222px; }
  .about h2 { font-size: 19px; font-weight: 700; color: var(--purple); margin-bottom: 12px; }
  .about p { font-weight: 300; font-size: 15.5px; line-height: 22.5px; color: var(--ink); }

  .summit-image { position: absolute; left: 660px; top: 640px; width: 185px; height: 435px; }

  .cta-band {
    position: absolute; left: 0; top: 1075px; width: 845px; height: 125px;
    background: var(--purple); color: var(--white);
    font-family: "Oswald", "Arial Narrow", sans-serif; text-transform: uppercase;
  }
  .cta-band__title { position: absolute; left: 36px; top: 22px; font-size: 22px; font-weight: 500; }
  .cta-band__text {
    position: absolute; left: 36px; top: 54px; width: 360px;
    font-size: 14px; line-height: 20px; font-weight: 400;
  }
  .cta-band__text .accent { color: var(--teal); }
  .cta-band__chevron { position: absolute; left: 392px; top: 52px; width: 16px; height: 24px; }
  .cta-band__email {
    position: absolute; left: 424px; top: 44px;
    font-size: 28px; font-weight: 400; text-transform: none; letter-spacing: 0.3px;
  }
</style>
</head>
<body>
<main class="flyer">
  <svg class="backdrop" width="845" height="1200" viewBox="0 0 845 1200" aria-hidden="true">
    <defs>
      <linearGradient id="sweep" x1="0" y1="0" x2="1" y2="0">
        <stop offset="0" stop-color="#ffffff"/>
        <stop offset="0.6" stop-color="#ececec"/>
        <stop offset="1" stop-color="#dedede"/>
      </linearGradient>
      <radialGradient id="wheel" cx="0.5" cy="0.5" r="0.5">
        <stop offset="0.55" stop-color="#d6d6d6"/>
        <stop offset="1" stop-color="#efefef"/>
      </radialGradient>
      <radialGradient id="hub" cx="0.5" cy="0.5" r="0.5">
        <stop offset="0" stop-color="#ffffff"/>
        <stop offset="0.7" stop-color="#f4f4f4"/>
        <stop offset="1" stop-color="#dddddd"/>
      </radialGradient>
    </defs>
    <!-- top sweep -->
    <path d="M0 0 H845 V90 C700 40 520 20 300 60 C180 80 80 90 0 70 Z" fill="url(#sweep)"/>
    <path d="M380 0 C520 30 700 50 845 40" fill="none" stroke="#ffffff" stroke-width="3"/>
    <!-- wheel -->
    <circle cx="423" cy="420" r="300" fill="url(#wheel)"/>
    <circle cx="423" cy="420" r="258" fill="none" stroke="#ffffff" stroke-width="16"/>
    <circle cx="423" cy="420" r="205" fill="url(#hub)"/>
    <circle cx="423" cy="420" r="205" fill="none" stroke="#ffffff" stroke-width="6"/>
    <!-- are you arrow -->
    <polygon points="0,163 148,163 148,150 208,192 148,233 148,221 0,221" fill="var(--purple)"/>
    <!-- question bubbles -->
    <g fill="var(--teal)">
      <circle cx="423" cy="185" r="108"/>
      <polygon points="405,286 441,286 423,318"/>
      <circle cx="132" cy="412" r="108"/>
      <polygon points="232,394 232,430 246,412"/>
      <circle cx="725" cy="412" r="108"/>
      <polygon points="620,394 620,430 600,412"/>
      <circle cx="423" cy="630" r="108"/>
      <polygon points="405,530 441,530 423,516"/>
    </g>
    <!-- hub mark -->
    <circle cx="408" cy="370" r="22" fill="var(--teal)"/>
  </svg>

  <div class="are-you">Are You:</div>

  <p class="question question--top">Fed up<br>but unsure<br>how to<br>move on?</p>
  <p class="question question--left">Contemplating<br>what the next<br>year could<br>bring?</p>
  <p class="question question--right">Finding<br>it hard to<br>focus?</p>
  <p class="question question--bottom">Looking for<br>new<br>opportunities<br>&amp; possibilities?</p>

  <blockquote class="quote">
    The secret of change<br>is to focus all of your energy<br>not on fighting the old, but on<br>building the new
    <cite>- Elias Varro</cite>
  </blockquote>

  <div class="brand">
    <span class="brand__dot"></span>
    <p class="brand__name">Reaching Your<br>Summit</p>
  </div>

  <section class="programme">
    <p>Take the first<br>step towards a<br>happier life now<br>by taking up your own,<br>personally tailored <strong>‘Clear<br>tides’</strong> coaching programme.</p>
    <p>The Clear tides programme consists of <span class="highlight">6 face to face</span> confidential coaching sessions <span class="highlight">60-90 minutes.</span> Each session is carefully designed around you, <span class="highlight">your needs</span> and <span class="highlight">goals.</span> You will also benefit from bespoke email support in between sessions, <em>development feedback</em>, <em>recommended resources</em> to support your journey and a bespoke <em>action plan</em>.</p>
    <p>This programme will help you achieve your goals and increase your satisfaction with your work and home life.</p>
  </section>

  <div class="divider"></div>

  <section class="about">
    <h2>Why work with me?</h2>
    <p>I’m a coach and transformational leader with a decade of experience in delivering better results for individuals, organisations and customers. I’m passionate about helping people achieve their potential and find new possibilities.</p>
  </section>

  <svg class="summit-image" viewBox="0 0 185 435" role="img" aria-label="Silhouette of a person standing on a cliff top with a raised fist">
    <defs>
      <linearGradient id="summitFade" x1="0" y1="0" x2="0" y2="1">
        <stop offset="0" stop-color="#ffffff"/>
        <stop offset="1" stop-color="#1a1a1a"/>
      </linearGradient>
    </defs>
    <rect width="185" height="435" fill="url(#summitFade)"/>
  </svg>

  <footer class="cta-band">
    <p class="cta-band__title">Take the first step now:</p>
    <p class="cta-band__text"><span class="accent">Contact me today</span> and book a <span class="accent">complimentary 15 min phone</span> or <span class="accent">video</span> consultation by emailing me at:</p>
    <svg class="cta-band__chevron" viewBox="0 0 16 24" aria-hidden="true">
      <path d="M2 4 L8 12 L2 20 M8 4 L14 12 L8 20" fill="none" stroke="#8a7aa8" stroke-width="1.5"/>
    </svg>
    <p class="cta-band__email">hello@reachingyoursummit.com</p>
  </footer>
</main>
</body>
</html>
```